Website Design For Ecommerce Brand That Sells Personalized Wall Decor

We need a new website for our company Copper Lantern. Our current site is functioning through wordpress/woocomerce but we are not happy with the appearance. Our products really wow people when they receive them and we need your help making our website do the same!

Number of Pages Required

4 page

```html
<!DOCTYPE html>
<html lang="en">
<head>
<meta charset="utf-8">
<title>Copper Lantern – Website Pages</title>
<link href="https://fonts.googleapis.com/css2?family=Open+Sans:wght@400;600;700&display=swap" rel="stylesheet">
<style>
:root{
  --sage:#7b9c7d;
  --sage-dark:#5f8262;
  --sage-light:#b8dcc0;
  --dark:#1f1b15;
  --ink:#2b2b2b;
  --muted:#7a7a7a;
  --line:#e3e3e3;
  --panel:#f2f2f2;
  --star:#f0b400;
  --canvas:#f1f2f4;
}
*{box-sizing:border-box;margin:0;padding:0}
html,body{width:1045px;height:1200px;overflow:hidden;background:var(--canvas);font-family:"Open Sans",Arial,sans-serif;color:var(--ink)}
.stage{position:absolute;left:0;top:0;width:1792px;height:2057px;transform:scale(.58315);transform-origin:0 0}
.page{position:absolute;width:476px;background:#fff;overflow:hidden;box-shadow:0 0 4px rgba(0,0,0,.12)}
.abs{position:absolute}

/* header */
.topbar{position:absolute;left:0;top:0;width:476px;height:15px;background:var(--sage);color:#fff;font-size:5px;display:flex;align-items:center;justify-content:space-between;padding:0 44px}
.topbar .contact{display:flex;gap:10px;align-items:center}
.dot{display:inline-block;width:7px;height:7px;border:1px solid #fff;border-radius:50%;vertical-align:middle;margin-right:2px}
.topbar .socials{display:flex;gap:6px}
.topbar .socials i{width:4px;height:4px;background:#fff;border-radius:50%;display:block}
.nav{position:absolute;left:0;top:15px;width:476px;height:32px;display:flex;align-items:center;padding-left:99px;font-size:5.5px;font-weight:600;gap:9px}
.nav .active{color:var(--sage)}
.search{width:84px;height:13px;border:1px solid var(--line);font-size:5px;font-weight:400;color:var(--muted);display:flex;align-items:center;justify-content:space-between;padding:0 4px;margin-left:2px}
.icons{display:flex;gap:3px;margin-left:3px}
.icons i{width:10px;height:10px;border:1px solid var(--sage);border-radius:50%;display:block}
.login{background:var(--sage);color:#fff;font-size:5px;padding:4px 9px;margin-left:6px}
.logo-badge{position:absolute;left:46px;top:18px;width:45px;height:45px;border-radius:50%;background:#fff;z-index:3;display:flex;align-items:center;justify-content:center;text-align:center;font-size:6.5px;font-weight:600;line-height:1.05;color:var(--dark)}

/* hero */
.hero{position:absolute;left:0;top:47px;width:476px;background:linear-gradient(100deg,#5d4a3a 0%,#7b7f8d 32%,#6f89a9 62%,#6a84a5 100%)}
.hero .wave{position:absolute;left:0;bottom:0;width:476px;height:70px}
.hero-title{position:absolute;color:#fff;font-weight:700;letter-spacing:.3px;text-align:center}
.arrow{position:absolute;width:13px;height:13px;border:1px solid #fff;border-radius:50%}

/* shared bits */
.section-title{position:absolute;left:0;width:476px;text-align:center;font-size:11px;font-weight:700}
.btn{display:inline-block;background:var(--sage);color:#fff;font-size:5px;font-weight:600;padding:4px 9px}
.stars{color:var(--star);font-size:6px;letter-spacing:1px}
.photo{display:block}

/* product cards */
.grid{position:absolute;left:47px;display:grid;grid-template-columns:repeat(4,88px);gap:9px}
.card{height:138px;border:1px solid var(--line);box-shadow:0 1px 3px rgba(0,0,0,.08);text-align:center;padding:2px}
.card .photo{height:70px;background:linear-gradient(135deg,#8a6d55,#cbb79e)}
.card .price{color:var(--sage);font-size:6px;font-weight:700;margin:2px 0}
.card .name{font-size:4.6px;font-weight:600;line-height:1.3;height:13px}
.card .actions{display:flex;justify-content:center;gap:5px;margin-top:4px;align-items:center}
.card .actions .btn{border-radius:6px;padding:3px 7px;font-size:4.5px}
.cart{width:10px;height:10px;border:1px solid var(--muted);border-radius:50%}

/* footer */
.footer{position:absolute;left:0;width:476px}
.footer svg{display:block;width:476px;height:45px}
.footer .body{background:var(--dark);color:#fff;height:112px;position:relative}
.footer .brand{position:absolute;left:42px;top:10px;width:70px;text-align:center;font-size:12px;line-height:1.1;font-weight:400}
.footer .soc{position:absolute;left:42px;top:66px;display:flex;gap:6px}
.footer .soc i{width:11px;height:11px;border:1px solid #fff;border-radius:50%;display:block}
.fcol{position:absolute;top:7px;font-size:5px;line-height:2.7}
.fcol h4{font-size:5px;font-weight:700;margin-bottom:3px}
.fcol .row{display:flex;gap:5px;align-items:flex-start;line-height:1.5;margin-bottom:7px}
.fcol .row .dot{width:10px;height:10px;flex:none}
.footer .bar{background:var(--sage);height:23px;display:flex;align-items:center;justify-content:center;gap:14px;color:#fff;font-size:4.2px}
.cards{display:flex;gap:3px}
.cards i{width:15px;height:8px;background:#fff;border-radius:1px;display:block}

/* reviews */
.review{position:absolute;width:189px;height:80px;border:1px solid var(--line);box-shadow:0 1px 4px rgba(0,0,0,.1);font-size:5px;line-height:1.65;color:var(--muted);padding:10px 8px}
.reviewer{position:absolute;display:flex;align-items:center;gap:6px;font-size:5px}
.avatar{width:18px;height:18px;border-radius:50%;background:#9aa3a8}
.reviewer b{color:var(--sage);font-weight:600;display:block}

/* faq */
.faq{position:absolute;left:44px;width:388px;background:#f4f4f4;box-shadow:0 1px 3px rgba(0,0,0,.1);font-size:5.2px;font-weight:600}
.faq .q{height:23px;display:flex;align-items:center;justify-content:space-between;padding:0 20px}
.faq .q i{width:5px;height:5px;background:var(--dark);border-radius:50%}
.faq .a{background:#fff;margin:0 3px 3px;padding:10px 17px;font-weight:400;line-height:1.75;color:#555;font-size:5px}

/* product detail */
.ticks{list-style:none;font-size:5px;color:#555}
.ticks li{display:flex;align-items:center;gap:4px;height:11.9px}
.ticks li::before{content:"";width:5px;height:5px;border-radius:50%;background:var(--sage);flex:none}

/* contact form */
.field{position:absolute;height:15px;border:1px solid var(--line);background:#fff;font-size:4.6px;padding:4px 6px;color:#555}
</style>
</head>
<body>
<div class="stage">

<!-- ================= HOME ================= -->
<section class="page" style="left:100px;top:86px;height:1886px">
  <div class="topbar"><div class="contact"><span><span class="dot"></span>+ 100 (555) 0142</span><span><span class="dot"></span>support@copperlantern.com</span></div><div class="socials"><i></i><i></i><i></i><i></i></div></div>
  <div class="logo-badge">COPPER<br>LANTERN</div>
  <nav class="nav"><span class="active">HOME</span><span>PRODUCTS</span><span>FAQ</span><span>CONTACT US</span><span class="search">Search <span>⌕</span></span><span class="icons"><i></i><i></i><i></i></span><span class="login">LOGIN ➜</span></nav>
  <div class="hero" style="height:305px" role="img" aria-label="Tiered tray of personalised wooden decor on a rustic table">
    <div class="arrow" style="left:17px;top:113px"></div>
    <div class="arrow" style="left:446px;top:98px"></div>
    <div class="abs" style="left:302px;top:66px;color:#fff">
      <div style="font-size:11px;font-weight:600">WELCOME TO</div>
      <div style="font-size:16px;font-weight:600;margin-top:1px">COPPER LANTERN</div>
      <div style="font-size:5.5px;line-height:1.7;margin-top:2px">Don't mind the mess as we finish up with<br>the new website design</div>
      <div class="btn" style="margin-top:10px">GET STARTED ➜</div>
    </div>
    <svg class="wave" viewBox="0 0 476 70" preserveAspectRatio="none"><path d="M0 38 Q250 85 476 0 L476 70 L0 70Z" fill="var(--sage-light)"/><path d="M0 48 Q250 88 476 14 L476 70 L0 70Z" fill="var(--sage)"/><path d="M0 52 Q250 92 476 22 L476 70 L0 70Z" fill="#fff"/></svg>
  </div>

  <div class="section-title" style="top:335px">NEW ARRIVALS</div>
  <div class="abs" style="left:121px;top:357px;display:flex;gap:5px;font-size:4.6px;font-weight:600">
    <span style="background:var(--sage);color:#fff;padding:4px 13px;border-radius:7px">ALL</span>
    <span style="background:#eef0ee;color:var(--sage);padding:4px 17px;border-radius:7px">GNOME</span>
    <span style="background:#eef0ee;color:var(--sage);padding:4px 5px;border-radius:7px">PERSONALIZED FAMILY TREE</span>
    <span style="background:#eef0ee;color:var(--sage);padding:4px 6px;border-radius:7px">HOME DECOR</span>
  </div>
  <div class="grid" style="top:384px">
    <div class="card"><div class="photo" role="img" aria-label="Round wooden pet memorial ornament"></div><div class="stars">★★★★★</div><div class="price">$16.00</div><div class="name">In Memory of Lost<br>Pet Ornament</div><div class="actions"><span class="btn">SHOP NOW</span><span class="cart"></span></div></div>
    <div class="card"><div class="photo" role="img" aria-label="Wooden mitten family ornament"></div><div class="stars">★★★★★</div><div class="price">$17.00</div><div class="name">Custom Family Christmas<br>Ornament – Mittens</div><div class="actions"><span class="btn">SHOP NOW</span><span class="cart"></span></div></div>
    <div class="card"><div class="photo" role="img" aria-label="Framed family tree wall decor"></div><div class="stars">★★★★★</div><div class="price">$62.00</div><div class="name">12 Inch Square<br>Framed Personalized</div><div class="actions"><span class="btn">SHOP NOW</span><span class="cart"></span></div></div>
    <div class="card"><div class="photo" style="background:linear-gradient(135deg,#cfcfcf,#f0f0f0)" role="img" aria-label="Unfinished wooden mushroom cutout"></div><div class="stars">★★★★★</div><div class="price">$30.00</div><div class="name">12 Inch Square<br>Framed Personalized</div><div class="actions"><span class="btn">SHOP NOW</span><span class="cart"></span></div></div>
    <div class="card"><div class="photo" role="img" aria-label="Pet memorial plaque"></div><div class="stars">★★★★★</div><div class="price">20.00</div><div class="name">In Memory of Lost Pet<br>Plaque, Custom Memorial</div><div class="actions"><span class="btn">SHOP NOW</span><span class="cart"></span></div></div>
    <div class="card"><div class="photo" style="background:linear-gradient(135deg,#d8d2c8,#f3efe8)" role="img" aria-label="Faux shiplap family tree sign"></div><div class="stars">★★★★★</div><div class="price">$69.00</div><div class="name">Faux Shiplap Personalized<br>Family Tree</div><div class="actions"><span class="btn">SHOP NOW</span><span class="cart"></span></div></div>
    <div class="card"><div class="photo" style="background:linear-gradient(135deg,#5a4a40,#b9b2aa)" role="img" aria-label="Wooden gnome ornament"></div><div class="stars">★★★★★</div><div class="price">$62.00</div><div class="name">In Memory of Lost<br>Pet Ornament</div><div class="actions"><span class="btn">SHOP NOW</span><span class="cart"></span></div></div>
    <div class="card"><div class="photo" style="background:linear-gradient(135deg,#cfcfcf,#f2f2f2)" role="img" aria-label="Unfinished wooden pumpkin cutout"></div><div class="stars">★★★★★</div><div class="price">$16.00</div><div class="name">In Memory of Lost<br>Pet Ornament</div><div class="actions"><span class="btn">SHOP NOW</span><span class="cart"></span></div></div>
  </div>

  <div class="abs" style="left:0;top:702px;width:240px;height:184px;background:linear-gradient(160deg,#9aa6b4,#6d5a48 60%,#4a3a2e)" role="img" aria-label="Collage of family tree signs and framed trees"></div>
  <div class="abs" style="left:240px;top:702px;width:236px;height:184px;background:var(--sage);color:#fff;text-align:center;padding-top:22px">
    <div style="font-size:10px;font-weight:600">PERSONALIZE</div>
    <div style="font-size:15px;font-weight:600;margin-top:2px">THE FAMILY TREE</div>
    <div style="font-size:5px;line-height:1.75;margin:8px 20px 0">Lorem ipsum dolor sit amet, consectetur adipiscing elit, sed do eiusmod tempor incididunt ut labore et dolore magna aliqua.Ut enim ad minim veniam, quis nostrud exercitation</div>
    <div style="display:inline-block;border:1px solid #fff;font-size:5px;padding:5px 13px;margin-top:10px">Read More</div>
  </div>

  <div class="section-title" style="top:917px">OUR REVIEWS</div>
  <div class="review" style="left:45px;top:946px">Sed perspiciati error voluptatem accusantium indoloremique laudantium aperiam eaque ipsnrxa quae inventore inveritatis quasi odit architinecto beatae vitae dicta sunt odit explicbo. Nemo enim ipsat voluptatem quia voluptasin aspernatur aut aut fugitquia consequuntur magni dolores qui at rationeuasi architectt fugit aut dicta soditsed beatae vitae dicta odit.</div>
  <div class="review" style="left:242px;top:946px">Sed perspiciati error voluptatem accusantium indoloremique laudantium aperiam eaque ipsnrxa quae inventore inveritatis quasi odit architinecto beatae vitae dicta sunt odit explicbo. Nemo enim ipsat voluptatem quia voluptasin aspernatur aut aut fugitquia consequuntur magni dolores qui at rationeuasi architectt fugit aut dicta soditsed beatae vitae dicta odit.</div>
  <div class="reviewer" style="left:63px;top:1038px"><span class="avatar" role="img" aria-label="Reviewer photo"></span><span><b>NORA BELL</b>Lorem ipsum dolor sit</span><span class="stars" style="margin-left:28px">★★★★★</span></div>
  <div class="reviewer" style="left:260px;top:1038px"><span class="avatar" role="img" aria-label="Reviewer photo"></span><span><b>OWEN PARK</b>Lorem ipsum dolor sit</span><span class="stars" style="margin-left:28px">★★★★★</span></div>

  <div class="abs" style="left:0;top:1091px;width:476px;height:207px;background:linear-gradient(100deg,#4a3527,#5e4331 45%,#3c2a1f)" role="img" aria-label="Personalised name ornament on a dark wooden table">
    <div class="abs" style="left:228px;top:42px;width:200px;color:#fff">
      <div style="font-size:10.5px;font-weight:600">COPPER LANTERN VARIATIONS</div>
      <div style="font-size:5.5px;line-height:1.95;margin-top:6px">Lorem ipsum dolor sit amet, consectetur adipiscing elit, sed do eiusmod tempor incididunt ut labore et dolore magna aliqua. Ut enim ad minim veniam, quis nostrud exercitation ullamco laboris nisi ut aliquip ex ea commodo ut consequat. Duis aute irure dolor in reprehenderit in voluptate velit esse cillum dolore eu fugiat nulla pariaturLorem ipsum dolor sit</div>
      <div class="btn" style="margin-top:9px;padding:5px 10px">SHOP NOW</div>
    </div>
  </div>

  <div class="abs" style="left:0;top:1298px;width:476px;height:117px;background:var(--sage-light);text-align:center">
    <div style="font-size:11px;font-weight:600;margin-top:24px">GET IN TOUCH</div>
    <div style="font-size:5.5px;margin-top:8px;color:#444">Don't miss latest updates &amp; hot deals</div>
    <div style="margin:12px auto 0;width:252px;height:24px;background:#fff;display:flex;align-items:center;justify-content:space-between;padding:3px 3px 3px 9px;font-size:5px">
      <span>✉ &nbsp;Email Address</span><span style="background:var(--sage-light);font-weight:700;color:#2f4a33;height:18px;display:flex;align-items:center;padding:0 10px">SIGNUP</span>
    </div>
  </div>

  <div class="section-title" style="top:1446px">FOLLOW US INSTAGRAM</div>
  <div class="abs" style="left:45px;top:1476px;width:387px;height:168px;display:grid;grid-template-columns:repeat(4,1fr);grid-template-rows:repeat(2,1fr);gap:2px">
    <div style="background:linear-gradient(135deg,#6b5a4b,#d8d6d2)" role="img" aria-label="Wooden gnome photo"></div>
    <div style="background:linear-gradient(135deg,#3a3a3a,#6e6a66)" role="img" aria-label="Framed family tree photo"></div>
    <div style="background:linear-gradient(135deg,#4a3e35,#d6d3cf)" role="img" aria-label="Blank wooden shapes photo"></div>
    <div style="background:linear-gradient(135deg,#c98ac8,#e5c65a 50%,#5ea65a)" role="img" aria-label="Rainbow painted gnome photo"></div>
    <div style="background:linear-gradient(135deg,#b09080,#dcb9a0)" role="img" aria-label="Together sign photo"></div>
    <div style="background:linear-gradient(135deg,#8a6d55,#d9c8b4)" role="img" aria-label="Mitten ornament photo"></div>
    <div style="background:linear-gradient(135deg,#3e7a3a,#d9a8c4)" role="img" aria-label="Painted green gnome photo"></div>
    <div style="background:linear-gradient(135deg,#4a3f36,#8c8680)" role="img" aria-label="Framed family tree photo"></div>
  </div>
  <div class="btn abs" style="left:211px;top:1661px;padding:6px 9px">FOLLOW US</div>

  <div class="footer" style="top:1706px">
    <svg viewBox="0 0 476 45" preserveAspectRatio="none"><path d="M0 30 Q238 -20 476 30 L476 45 L0 45Z" fill="var(--sage-light)"/><path d="M0 36 Q238 -8 476 36 L476 45 L0 45Z" fill="var(--dark)"/></svg>
    <div class="body" style="height:112px">
      <div class="brand">COPPER<br>LANTERN</div>
      <div class="soc"><i></i><i></i><i></i><i></i></div>
      <div class="fcol" style="left:155px"><h4>QUICKLINKS</h4>Home<br>Products<br>FAQ<br>Contact Us</div>
      <div class="fcol" style="left:234px"><h4>SUPPORT</h4>FAQ<br>Terms &amp; Conditions<br>Contact us<br>Privacy Policy</div>
      <div class="fcol" style="left:335px"><h4>CONTACT US</h4><div class="row"><span class="dot"></span>+ 100 (555) 0142</div><div class="row"><span class="dot"></span>support@copperlantern.com</div><div class="row"><span class="dot"></span>12,Lorem ipsum dolor ant<br>consectetur adipiscing elit</div></div>
    </div>
    <div class="bar"><span>© Copyrights 2022 Copper Lantern All Right Reserved.</span><span class="cards"><i></i><i></i><i></i><i></i><i></i><i></i><i></i></span></div>
  </div>
</section>

<!-- ================= PRODUCT ================= -->
<section class="page" style="left:658px;top:86px;height:927px">
  <div class="topbar"><div class="contact"><span><span class="dot"></span>+ 100 (555) 0142</span><span><span class="dot"></span>support@copperlantern.com</span></div><div class="socials"><i></i><i></i><i></i><i></i></div></div>
  <div class="logo-badge">COPPER<br>LANTERN</div>
  <nav class="nav"><span>HOME</span><span class="active">PRODUCTS</span><span>FAQ</span><span>CONTACT US</span><span class="search">Search <span>⌕</span></span><span class="icons"><i></i><i></i><i></i></span><span class="login">LOGIN ➜</span></nav>
  <div class="hero" style="height:215px" role="img" aria-label="Tiered tray of personalised wooden decor on a rustic table">
    <div class="hero-title" style="left:230px;top:85px;font-size:24px">PRODUCT</div>
    <svg class="wave" viewBox="0 0 476 70" preserveAspectRatio="none"><path d="M0 40 Q250 85 476 0 L476 70 L0 70Z" fill="var(--sage-light)"/><path d="M0 50 Q250 88 476 14 L476 70 L0 70Z" fill="var(--sage)"/><path d="M0 54 Q250 92 476 22 L476 70 L0 70Z" fill="#fff"/></svg>
  </div>

  <div class="abs" style="left:44px;top:291px;width:196px;height:184px;background:linear-gradient(135deg,#5b7a4e,#3f3027 30%,#5b4a3c 70%,#8a7058)" role="img" aria-label="Framed family tree wall decor with names on hearts"></div>
  <div class="abs" style="left:44px;top:479px;display:flex;gap:3px">
    <div style="width:36px;height:28px;background:#6a5a4c" role="img" aria-label="Thumbnail"></div>
    <div style="width:36px;height:28px;background:#4e4238" role="img" aria-label="Thumbnail"></div>
    <div style="width:36px;height:28px;background:#5a4c40" role="img" aria-label="Thumbnail"></div>
    <div style="width:36px;height:28px;background:#6e655c" role="img" aria-label="Thumbnail"></div>
    <div style="width:36px;height:28px;background:#3f3a36" role="img" aria-label="Thumbnail"></div>
  </div>

  <div class="abs" style="left:261px;top:290px;width:172px">
    <div style="font-size:6.5px;font-weight:600;line-height:1.4">12 INCH SQUARE FRAMED PERSONALIZED<br>FAMILY TREE WALL DECOR</div>
    <div style="display:flex;gap:4px;margin-top:5px"><span class="cart" style="width:13px;height:13px;border-color:var(--sage)"></span><span class="cart" style="width:13px;height:13px;border-color:var(--sage)"></span><span class="cart" style="width:13px;height:13px;border-color:var(--sage)"></span><span class="cart" style="width:13px;height:13px;border-color:var(--sage)"></span></div>
    <div class="stars" style="margin-top:5px">★★★★★</div>
    <div style="font-size:10px;font-weight:600;margin-top:3px">$62.00</div>
    <div style="font-size:5px;font-weight:700;margin-top:5px">HEADLINE</div>
    <div style="font-size:5px;margin-top:5px">"Grandkids", "Our Family", "The Smiths"</div>
    <div style="font-size:5px;font-weight:600;color:var(--sage);margin-top:6px;margin-bottom:2px">PERSONALIZE YOUR TREE BELOW</div>
    <ul class="ticks">
      <li>Enter all names you would like on the hearts along</li>
      <li>with description:</li>
      <li>Please Separate By Pressing "ENTER" on your keyboard:</li>
      <li>Special Instructions Feel Free To Email Us Directly</li>
      <li>Perfect Example How To Explain Hearts To Us:</li>
      <li>Middle of tree: (2" heart/ grandparents): Bob &amp; Sue</li>
      <li>Family 1: John (kid) Mary (spouse)</li>
      <li>Mike, Stacy (Mike's Spouse), Beth, Jackson (grandkids)</li>
      <li>Mason (great grand kid-son of Mike and Stacy)</li>
      <li>Rover, Spot (dogs)</li>
      <li>Family 2: Jennifer (kid) Lou (spouse)</li>
      <li>Riley, Kristen, Lilly (grandkids)</li>
      <li>Max (dog)</li>
      <li>Family 3: Matt (kid)</li>
      <li>Sandra (grandkid)</li>
      <li>Midnight, Sam (cats)</li>
    </ul>
    <div style="font-size:5px;color:#555;line-height:1.75;margin-top:6px;padding-left:7px;position:relative">Item can also be shipped without placement IF you so choose to attach the hearts yourself. Hearts are easily attached with wood glue.<span class="abs" style="left:0;top:9px;width:2.5px;height:2.5px;background:#222;border-radius:50%"></span></div>
    <div style="font-size:5px;color:#555;line-height:1.75;margin-top:5px;padding-left:7px;position:relative">Don't forget we will reach out with a photo for approval and if you would like that to be in a text on your cell then leave your number in the Notes section.<span class="abs" style="left:0;top:9px;width:2.5px;height:2.5px;background:#222;border-radius:50%"></span></div>
    <div style="height:30px;border:1px solid var(--line);margin-top:7px"></div>
    <div style="display:flex;gap:4px;margin-top:7px;align-items:center;font-size:5px">
      <span style="display:flex;border:1px solid var(--line)"><span style="width:10px;text-align:center;line-height:12px">-</span><span style="width:14px;text-align:center;line-height:12px;border-left:1px solid var(--line);border-right:1px solid var(--line)">1</span><span style="width:10px;text-align:center;line-height:12px">+</span></span>
      <span class="btn" style="margin-left:2px">Add To Cart</span>
    </div>
  </div>

  <div class="footer" style="top:748px">
    <svg viewBox="0 0 476 45" preserveAspectRatio="none"><path d="M0 30 Q238 -20 476 30 L476 45 L0 45Z" fill="var(--sage-light)"/><path d="M0 36 Q238 -8 476 36 L476 45 L0 45Z" fill="var(--dark)"/></svg>
    <div class="body" style="height:111px">
      <div class="brand">COPPER<br>LANTERN</div>
      <div class="soc"><i></i><i></i><i></i><i></i></div>
      <div class="fcol" style="left:155px"><h4>QUICKLINKS</h4>Home<br>Products<br>FAQ<br>Contact Us</div>
      <div class="fcol" style="left:234px"><h4>SUPPORT</h4>FAQ<br>Terms &amp; Conditions<br>Contact us<br>Privacy Policy</div>
      <div class="fcol" style="left:335px"><h4>CONTACT US</h4><div class="row"><span class="dot"></span>+ 100 (555) 0142</div><div class="row"><span class="dot"></span>support@copperlantern.com</div><div class="row"><span class="dot"></span>12,Lorem ipsum dolor ant<br>consectetur adipiscing elit</div></div>
    </div>
    <div class="bar"><span>© Copyrights 2022 Copper Lantern All Right Reserved.</span><span class="cards"><i></i><i></i><i></i><i></i><i></i><i></i><i></i></span></div>
  </div>
</section>

<!-- ================= FAQ ================= -->
<section class="page" style="left:1216px;top:86px;height:650px">
  <div class="topbar"><div class="contact"><span><span class="dot"></span>+ 100 (555) 0142</span><span><span class="dot"></span>support@copperlantern.com</span></div><div class="socials"><i></i><i></i><i></i><i></i></div></div>
  <div class="logo-badge">COPPER<br>LANTERN</div>
  <nav class="nav"><span>HOME</span><span>PRODUCTS</span><span class="active">FAQ</span><span>CONTACT US</span><span class="search">Search <span>⌕</span></span><span class="icons"><i></i><i></i><i></i></span><span class="login">LOGIN ➜</span></nav>
  <div class="hero" style="height:215px" role="img" aria-label="Tiered tray of personalised wooden decor on a rustic table">
    <div class="hero-title" style="left:210px;top:70px;font-size:19px;line-height:1.3">FREQUENTLY ASKED<br>QUESTIONS</div>
    <svg class="wave" viewBox="0 0 476 70" preserveAspectRatio="none"><path d="M0 40 Q250 85 476 0 L476 70 L0 70Z" fill="var(--sage-light)"/><path d="M0 50 Q250 88 476 14 L476 70 L0 70Z" fill="var(--sage)"/><path d="M0 54 Q250 92 476 22 L476 70 L0 70Z" fill="#fff"/></svg>
  </div>

  <div class="faq" style="top:294px"><div class="q">HOW SOON WILL I RECEIVE MY ORDER?<i></i></div></div>
  <div class="faq" style="top:326px"><div class="q">CAN I HAVE A PREVIEW OF MY PERSONALIZED TREE BEFORE IT'S SHIPPED?<i></i></div><div class="a">Absolutely! Just let us know at checkout and we will be sure to send you a picture before we glue anything down. We can send the image via Email or Txt to your cell phone, whichever you prefer, just be sure to include your phone number during checkout as well. In the event we are unsure about placement or have questions, we may send you a preview for your approval even if you didn't request it at checkout.</div></div>
  <div class="faq" style="top:420px"><div class="q">DO YOU SHIP OUT OF THE UNITED STATES?<i></i></div></div>

  <div class="footer" style="top:472px">
    <svg viewBox="0 0 476 45" preserveAspectRatio="none"><path d="M0 30 Q238 -20 476 30 L476 45 L0 45Z" fill="var(--sage-light)"/><path d="M0 36 Q238 -8 476 36 L476 45 L0 45Z" fill="var(--dark)"/></svg>
    <div class="body" style="height:111px">
      <div class="brand">COPPER<br>LANTERN</div>
      <div class="soc"><i></i><i></i><i></i><i></i></div>
      <div class="fcol" style="left:155px"><h4>QUICKLINKS</h4>Home<br>Products<br>FAQ<br>Contact Us</div>
      <div class="fcol" style="left:234px"><h4>SUPPORT</h4>FAQ<br>Terms &amp; Conditions<br>Contact us<br>Privacy Policy</div>
      <div class="fcol" style="left:335px"><h4>CONTACT US</h4><div class="row"><span class="dot"></span>+ 100 (555) 0142</div><div class="row"><span class="dot"></span>support@copperlantern.com</div><div class="row"><span class="dot"></span>12,Lorem ipsum dolor ant<br>consectetur adipiscing elit</div></div>
    </div>
    <div class="bar"><span>© Copyrights 2022 Copper Lantern All Right Reserved.</span><span class="cards"><i></i><i></i><i></i><i></i><i></i><i></i><i></i></span></div>
  </div>
</section>

<!-- ================= CONTACT ================= -->
<section class="page" style="left:658px;top:1077px;height:665px">
  <div class="topbar"><div class="contact"><span><span class="dot"></span>+ 100 (555) 0142</span><span><span class="dot"></span>support@copperlantern.com</span></div><div class="socials"><i></i><i></i><i></i><i></i></div></div>
  <div class="logo-badge">COPPER<br>LANTERN</div>
  <nav class="nav"><span>HOME</span><span>PRODUCTS</span><span>FAQ</span><span class="active">CONTACT US</span><span class="search">Search <span>⌕</span></span><span class="icons"><i></i><i></i><i></i></span><span class="login">LOGIN ➜</span></nav>
  <div class="hero" style="height:215px" role="img" aria-label="Tiered tray of personalised wooden decor on a rustic table">
    <div class="hero-title" style="left:243px;top:82px;font-size:22px">CONTACT US</div>
    <svg class="wave" viewBox="0 0 476 70" preserveAspectRatio="none"><path d="M0 40 Q250 85 476 0 L476 70 L0 70Z" fill="var(--sage-light)"/><path d="M0 50 Q250 88 476 14 L476 70 L0 70Z" fill="var(--sage)"/><path d="M0 54 Q250 92 476 22 L476 70 L0 70Z" fill="#fff"/></svg>
  </div>

  <div class="abs" style="left:44px;top:291px;width:387px;height:166px;background:var(--panel)">
    <div class="abs" style="left:32px;top:15px;font-size:6.5px;font-weight:700">CONTACT US</div>
    <div class="field" style="left:32px;top:33px;width:96px">Name:</div>
    <div class="field" style="left:131px;top:33px;width:96px">Email:</div>
    <div class="field" style="left:32px;top:52px;width:96px">Address:</div>
    <div class="field" style="left:131px;top:52px;width:96px">Subject:</div>
    <div class="field" style="left:32px;top:72px;width:195px;height:38px">Message:</div>
    <div class="btn abs" style="left:32px;top:121px;padding:5px 9px">SUBMIT ➜</div>
    <div class="abs" style="left:250px;top:15px;font-size:6.5px;font-weight:700">GET IN TOUCH WITH US</div>
    <div class="abs" style="left:250px;top:35px;font-size:5px;line-height:1.6">
      <div style="display:flex;gap:6px;margin-bottom:8px"><span class="cart" style="width:12px;height:12px;border-color:var(--sage);flex:none"></span><span><b>Phone Number :</b><br>100 (555) 0199</span></div>
      <div style="display:flex;gap:6px;margin-bottom:8px"><span class="cart" style="width:12px;height:12px;border-color:var(--sage);flex:none"></span><span><b>Email :</b><br>support@copperlantern.com</span></div>
      <div style="display:flex;gap:6px"><span class="cart" style="width:12px;height:12px;border-color:var(--sage);flex:none"></span><span><b>Address :</b><br>12,Lorem ipsum dolor ant<br>consectetur adipiscing elit</span></div>
    </div>
    <div class="abs" style="left:250px;top:126px;font-size:5px;font-weight:700">FOLLOW US</div>
    <div class="abs" style="left:250px;top:137px;display:flex;gap:4px"><span class="cart" style="width:10px;height:10px;border-color:var(--sage)"></span><span class="cart" style="width:10px;height:10px;border-color:var(--sage)"></span><span class="cart" style="width:10px;height:10px;border-color:var(--sage)"></span><span class="cart" style="width:10px;height:10px;border-color:var(--sage)"></span></div>
  </div>

  <div class="footer" style="top:487px">
    <svg viewBox="0 0 476 45" preserveAspectRatio="none"><path d="M0 30 Q238 -20 476 30 L476 45 L0 45Z" fill="var(--sage-light)"/><path d="M0 36 Q238 -8 476 36 L476 45 L0 45Z" fill="var(--dark)"/></svg>
    <div class="body" style="height:110px">
      <div class="brand">COPPER<br>LANTERN</div>
      <div class="soc"><i></i><i></i><i></i><i></i></div>
      <div class="fcol" style="left:155px"><h4>QUICKLINKS</h4>Home<br>Products<br>FAQ<br>Contact Us</div>
      <div class="fcol" style="left:234px"><h4>SUPPORT</h4>FAQ<br>Terms &amp; Conditions<br>Contact us<br>Privacy Policy</div>
      <div class="fcol" style="left:335px"><h4>CONTACT US</h4><div class="row"><span class="dot"></span>+ 100 (555) 0142</div><div class="row"><span class="dot"></span>support@copperlantern.com</div><div class="row"><span class="dot"></span>12,Lorem ipsum dolor ant<br>consectetur adipiscing elit</div></div>
    </div>
    <div class="bar"><span>© Copyrights 2022 Copper Lantern All Right Reserved.</span><span class="cards"><i></i><i></i><i></i><i></i><i></i><i></i><i></i></span></div>
  </div>
</section>

</div>
</body>
</html>
```